Lien Post Card - (5.5 x 8.5)

FRONT OF POSTCARD
Is a Property Lien Putting Your Home at Risk?
HOA Liens • Tax Liens • Municipal Charges • Other Property-Related Liens
You may have options to resolve outstanding liens and protect your home.
A Refinance or Home Equity Line of Credit (HELOC) may help you:
✔ Pay off qualifying liens
✔ Consolidate debt into one manageable payment
✔ Access your home's equity
✔ Improve your financial flexibility
✔ Avoid additional penalties, fees, or collection actions
Don't wait until the situation becomes more difficult.
Call today for a confidential review of your options.
Bluegate Lending Partners, Inc.
(800) 647-2915 x 42
www.bluegatelendco.com
NMLS #381640
BACK OF POSTCARD
Your Home Equity Could Be the Solution
If you have received notices regarding:
• Delinquent Property Taxes
• HOA or Condo Association Assessments
• Municipal Utility Liens
• Special Assessments
• Other Property-Related Obligations
You may qualify for financing options designed to help satisfy those obligations and bring your property current.
Our experienced mortgage professionals can review your situation and discuss available programs, including:
• Cash-Out Refinancing
• Home Equity Lines of Credit (HELOCs)
• Home Equity Loans
• Debt Consolidation Solutions
Free Consultation • No Obligation
Contact Marcus Delaney today at (800) 647-2915 x42 or mdelaney@bluegatelendco.com (NMLS #57308)

```html
<!DOCTYPE html>
<html lang="en">
<head>
<meta charset="utf-8">
<title>Lien Postcard – Bluegate Lending Partners</title>
<link href="https://fonts.googleapis.com/css2?family=Poppins:ital,wght@0,400;0,500;0,600;0,700;0,800;1,400&display=swap" rel="stylesheet">
<style>
:root{
  --blue-deep:#0b3fa8;
  --blue:#1a5fd0;
  --blue-bright:#3d8ef0;
  --navy:#15276b;
  --gold:#d9ad55;
  --gold-light:#f1d79b;
  --cream:#f8ecd3;
  --charcoal:#2f2f33;
  --ink:#2a2f45;
  --white:#ffffff;
  --stage:#e4e4e4;
}
*{box-sizing:border-box;margin:0;padding:0}
html,body{width:913px;height:1200px;overflow:hidden}
body{background:var(--stage);font-family:'Poppins',sans-serif;position:relative;color:var(--ink)}
.card{position:absolute;left:116px;width:681px;height:440px;overflow:hidden;box-shadow:0 8px 24px rgba(0,0,0,.25)}
.front{top:116px;background:linear-gradient(180deg,#fbf1dc 0%,#f0d9a6 100%)}
.back{top:643px;background:var(--white)}
.abs{position:absolute}
h1,h2,h3{font-weight:400}

/* front */
.front-sky{left:0;top:0;width:100%;height:100%}
.headline{left:40px;top:28px;color:var(--white);font-size:31px;line-height:1.2;font-weight:400;letter-spacing:-.3px}
.headline b{font-weight:800}
.brand-badge{left:520px;top:20px;width:112px;height:112px;border-radius:50%;background:var(--white);display:flex;flex-direction:column;align-items:center;justify-content:center;text-align:center;color:var(--navy);font-weight:700;font-size:15px;line-height:1.15}
.lien-band{left:40px;top:120px;width:601px;height:31px;background:linear-gradient(90deg,#e9c77c,#f3dba3,#e2b965);color:var(--navy);font-weight:600;font-size:14px;display:flex;align-items:center;justify-content:center;z-index:2}
.notice-band{left:60px;top:154px;width:556px;height:27px;background:var(--charcoal);color:var(--white);font-size:13px;font-weight:500;display:flex;align-items:center;justify-content:center;clip-path:polygon(3% 0,100% 0,97% 100%,0 100%);z-index:2}
.help-head{left:40px;top:200px;border-left:3px solid var(--blue);padding-left:7px;color:var(--navy);font-size:15.5px;line-height:1.2}
.help-head b{font-weight:700}
.help-list{left:40px;top:246px;list-style:none;font-size:11.5px;line-height:15.6px;color:var(--ink)}
.help-list li{display:flex;align-items:center;gap:6px}
.dot{width:8px;height:8px;border-radius:50%;background:radial-gradient(circle at 35% 35%,#f7dd9d,#c89a3c);flex:none}
.wait{left:40px;top:333px;color:var(--blue);font-size:13px}
.wait-pill{left:0;top:350px;width:321px;height:27px;background:var(--blue);border-radius:0 14px 14px 0;color:var(--white);font-size:14.5px;font-weight:500;padding-left:40px;display:flex;align-items:center}
.call{left:40px;top:389px;color:var(--blue);font-size:15px;line-height:1.15}
.call b{font-weight:800}
.photo{border-radius:50%;border:3px solid var(--white)}
.photo-man{left:353px;top:249px;width:122px;height:122px;background:linear-gradient(135deg,#6b7178,#3c3f44)}
.photo-couple{left:438px;top:176px;width:200px;height:200px;background:linear-gradient(135deg,#c9c3bb,#6c5f58 60%,#e3e1de)}
.company{left:298px;top:386px;font-size:11.5px;color:var(--navy);font-weight:500}
.phone-pill{left:298px;top:403px;height:24px;padding:0 12px 0 4px;background:var(--blue);border-radius:12px;color:var(--white);font-weight:700;font-size:14px;display:flex;align-items:center;gap:6px}
.phone-icon{width:18px;height:18px;border-radius:50%;background:var(--white);display:flex;align-items:center;justify-content:center}
.nmls{left:563px;top:396px;font-size:11px;color:var(--navy);font-weight:500}
.web{left:495px;top:411px;font-size:11px;color:var(--navy);font-weight:500;display:flex;align-items:center;gap:4px}

/* back */
.back-shape{left:0;top:0}
.back-head{left:40px;top:26px;font-size:19px;line-height:1.15;color:var(--navy);font-weight:400}
.back-head b{display:block;font-weight:800;color:var(--blue-deep);font-size:21px}
.notice-box{left:40px;top:77px;width:311px;height:100px;border-radius:8px;background:linear-gradient(135deg,var(--blue),var(--blue-bright) 60%,var(--blue));color:var(--white);padding:7px 12px}
.notice-box h3{font-size:13px;font-weight:500}
.notice-box h3 b{font-weight:700}
.list{list-style:none;font-size:9.5px;line-height:13.5px;margin-top:3px}
.list li{display:flex;align-items:center;gap:6px}
.list .dot{width:7px;height:7px}
.qualify{left:40px;top:183px;width:320px;font-size:9.5px;font-style:italic;line-height:1.35;color:#4a4a55}
.program-box{left:40px;top:215px;width:311px;height:105px;border-radius:8px 8px 0 0;background:linear-gradient(135deg,#e8c680,#f4deaa);padding:8px 12px;color:var(--ink)}
.program-box p{font-size:9.3px;line-height:1.35;font-weight:500}
.program-box .list{margin-top:5px;line-height:13.5px}
.bdot{width:7px;height:7px;border-radius:50%;background:var(--blue-bright);flex:none}
.free-bar{left:40px;top:317px;width:311px;height:25px;background:var(--blue);border-radius:0 0 0 8px;color:var(--white);font-weight:600;font-size:14px;display:flex;align-items:center;padding-left:10px}
.portrait{left:303px;top:232px;width:130px;height:130px;border-radius:50%;border:4px solid var(--blue-bright);background:linear-gradient(160deg,#b9c1c9,#3b3c44 70%)}
.contact{left:40px;top:348px;font-size:15px;color:var(--ink)}
.contact b{color:var(--blue-deep);font-weight:700}
.back-phone{left:40px;top:372px;height:27px;padding:0 16px 0 4px;border:2px solid var(--blue-bright);border-radius:14px;background:var(--white);color:var(--blue-deep);font-weight:700;font-size:16px;display:flex;align-items:center;gap:7px}
.back-phone .phone-icon{background:var(--blue);width:20px;height:20px}
.email{left:40px;top:408px;font-size:11.5px;color:#444}
.email span{margin-left:8px;padding-left:8px;border-left:1px solid var(--blue)}
.back-brand{left:420px;top:80px;width:140px;text-align:center;color:var(--navy);font-weight:700;font-size:15px;line-height:1.15}
.stamp{left:561px;top:41px;width:80px;height:79px;background:#d9d9d9}
.address-line{left:473px;width:168px;height:1px;background:#9a9a9a}
</style>
</head>
<body>

<section class="card front" aria-label="Postcard front">
  <svg class="abs front-sky" width="681" height="440" viewBox="0 0 681 440" aria-hidden="true">
    <defs>
      <linearGradient id="sky" x1="0" y1="0" x2="1" y2="0">
        <stop offset="0" stop-color="#0a3ea6"/>
        <stop offset=".6" stop-color="#2a75e0"/>
        <stop offset="1" stop-color="#5aa2f2"/>
      </linearGradient>
    </defs>
    <path d="M0 0H681V196C590 200 500 168 400 176C260 186 120 188 0 180Z" fill="url(#sky)"/>
    <path d="M0 180C120 188 260 186 400 176C500 168 590 200 681 196V206C590 210 500 180 400 186C260 196 120 198 0 190Z" fill="#ffffff" opacity=".9"/>
    <path d="M420 182C500 172 580 206 681 200V222C600 222 520 192 420 182Z" fill="#0c5a86"/>
  </svg>

  <h1 class="abs headline">IS A <b>PROPERTY LIEN</b> PUTTING<br>YOUR <b>HOME AT RISK?</b></h1>
  <div class="abs brand-badge">Bluegate<br>Lending</div>
  <div class="abs lien-band">HOA Liens • Tax Liens • Municipal Charges • Other Property-Related Liens</div>
  <div class="abs notice-band">You may have options to resolve outstanding liens and protect your home.</div>

  <h2 class="abs help-head">A Refinance or Home Equity<br>Line of Credit (HELOC) <b>may help you:</b></h2>
  <ul class="abs help-list">
    <li><span class="dot"></span>Pay off qualifying liens</li>
    <li><span class="dot"></span>Consolidate debt into one manageable payment</li>
    <li><span class="dot"></span>Access your home's equity</li>
    <li><span class="dot"></span>Improve your financial flexibility</li>
    <li><span class="dot"></span>Avoid additional penalties, fees, or collection actions</li>
  </ul>
  <p class="abs wait">Don't wait until the</p>
  <p class="abs wait-pill">situation becomes more difficult.</p>
  <p class="abs call"><b>CALL TODAY</b> for a confidential<br>review of your options.</p>

  <div class="abs photo photo-couple" role="img" aria-label="Photo of a worried couple reviewing bills at a laptop"></div>
  <div class="abs photo photo-man" role="img" aria-label="Photo of a stressed man with his head in his hands"></div>

  <p class="abs company">Bluegate Lending Partners, Inc.</p>
  <p class="abs phone-pill"><span class="phone-icon"><svg width="11" height="11" viewBox="0 0 24 24"><path fill="#1a5fd0" d="M6.6 10.8a15 15 0 0 0 6.6 6.6l2.2-2.2a1 1 0 0 1 1-.25 11.4 11.4 0 0 0 3.6.6 1 1 0 0 1 1 1V20a1 1 0 0 1-1 1A17 17 0 0 1 3 4a1 1 0 0 1 1-1h3.5a1 1 0 0 1 1 1c0 1.25.2 2.45.6 3.6a1 1 0 0 1-.25 1Z"/></svg></span>(800) 647-2915 x 42</p>
  <p class="abs nmls">NMLS #381640</p>
  <p class="abs web"><svg width="10" height="10" viewBox="0 0 24 24"><circle cx="12" cy="12" r="10" fill="none" stroke="#15276b" stroke-width="2"/><path d="M2 12h20M12 2c3 3 3 17 0 20M12 2c-3 3-3 17 0 20" fill="none" stroke="#15276b" stroke-width="2"/></svg>www.bluegatelendco.com</p>
</section>

<section class="card back" aria-label="Postcard back">
  <svg class="abs back-shape" width="681" height="441" viewBox="0 0 681 441" aria-hidden="true">
    <defs>
      <linearGradient id="sand" x1="0" y1="0" x2="1" y2="1">
        <stop offset="0" stop-color="#f6dda4"/>
        <stop offset="1" stop-color="#fbf0d8"/>
      </linearGradient>
    </defs>
    <path d="M0 0H390C470 90 520 260 395 441H0Z" fill="url(#sand)"/>
  </svg>

  <h2 class="abs back-head">YOUR HOME EQUITY<b>COULD BE THE SOLUTION</b></h2>

  <div class="abs notice-box">
    <h3>If you have <b>received notices</b> regarding:</h3>
    <ul class="list">
      <li><span class="dot"></span>Delinquent Property Taxes</li>
      <li><span class="dot"></span>HOA or Condo Association Assessments</li>
      <li><span class="dot"></span>Municipal Utility Liens</li>
      <li><span class="dot"></span>Special Assessments</li>
      <li><span class="dot"></span>Other Property-Related Obligations</li>
    </ul>
  </div>

  <p class="abs qualify">You may qualify for financing options designed to help satisfy those obligations and bring your property current.</p>

  <div class="abs program-box">
    <p>Our experienced mortgage professionals can review your situation and discuss available programs, including:</p>
    <ul class="list">
      <li><span class="bdot"></span>Cash-Out Refinancing</li>
      <li><span class="bdot"></span>Home Equity Lines of Credit (HELOCs)</li>
      <li><span class="bdot"></span>Home Equity Loans</li>
      <li><span class="bdot"></span>Debt Consolidation Solutions</li>
    </ul>
  </div>
  <p class="abs free-bar">Free Consultation • No Obligation</p>

  <div class="abs portrait" role="img" aria-label="Portrait photo of loan officer Marcus Delaney"></div>

  <p class="abs contact">Contact <b>Marcus Delaney</b> today at</p>
  <p class="abs back-phone"><span class="phone-icon"><svg width="12" height="12" viewBox="0 0 24 24"><path fill="#ffffff" d="M6.6 10.8a15 15 0 0 0 6.6 6.6l2.2-2.2a1 1 0 0 1 1-.25 11.4 11.4 0 0 0 3.6.6 1 1 0 0 1 1 1V20a1 1 0 0 1-1 1A17 17 0 0 1 3 4a1 1 0 0 1 1-1h3.5a1 1 0 0 1 1 1c0 1.25.2 2.45.6 3.6a1 1 0 0 1-.25 1Z"/></svg></span>(800) 647-2915 x42</p>
  <p class="abs email">mdelaney@bluegatelendco.com<span>(NMLS #57308)</span></p>

  <p class="abs back-brand">Bluegate<br>Lending</p>
  <div class="abs stamp" aria-label="Postage area"></div>
  <div class="abs address-line" style="top:215px"></div>
  <div class="abs address-line" style="top:255px"></div>
  <div class="abs address-line" style="top:294px"></div>
</section>

</body>
</html>
```